Dog Grooming Coupon Postcard

I need a postcard designed for my dog daycare, boarding and grooming business. This postcard will focus on the Grooming portion of my business. The design should be classy, easy to navigate, inviting and portray experience. We will use this item to mail to dog owners and place on shelves at veterinary clinics and other businesses.

Please find an attached file that can be used as the main graphic.

Information that must be included:
Business Name: The Velvet Kennel
Web Address: www.PlumeRetreats.example
Phone Number: 555-318-4096
Address: 2847 Larkspur Lane Millbrook, WI 54900
All of our service areas: Dog Grooming, Overnight Care, Daycare
Logo (I am trying to find our logo file, I will post when I have it. To design around it, go to our website to see what it looks like. It is a square with a paw.)

It would be nice to highlight that we are located in Millbrook.

I am open to having a map to show our location.

I want two offers/coupons available: (Please don't make these offers look like a standard coupon, i.e. dashed marks around two square boxes that look like grocery store coupons!)
First: New Client Offer - 20% Off Your Pet's First Grooming Visit
Second:15% Off Any Spa Package

Needs to include this disclaimer: Limit one coupon per household. Not valid with any other offers or coupons. Other restriction or exclusions may apply, call for details.

Our phone number must be large enough to easily read and easily be found.

If there is a way to include some of our grooming services with out taking away from the offers and call to action they include:
Organic Shampoo & Conditioner
Dental Care
Soothing Mud Baths
Flea & Tick Preventative
Shed-Less Treatment
Nail Trim
Haircut
Paw Massage
Spa Packages

I am open to different postcard sizing based on the design.

Target Market(s)

Dog owners who have a disposable income. Age range is 35-65. They are looking for trust and professionalism.

Industry/Entity Type

Grocery Store

Colors

Designer to choose colors to be used in the design.

Requirements
Must have
• Clean, neat design that is easy to read and navigate. Our phone number and a call to action such as, call today for an appointment or schedule an appointment today.

The new client offer should stand out.
Should not have
• Should not have clip art or cartoon looking graphics.

```html
<!DOCTYPE html>
<html lang="en">
<head>
<meta charset="utf-8">
<title>The Velvet Kennel – Grooming Postcard</title>
<link rel="stylesheet" href="https://fonts.googleapis.com/css2?family=PT+Sans+Narrow:wght@400;700&display=swap">
<style>
  :root {
    --stage: #ece9e4;
    --sky: #c2e4eb;
    --lime: #b3cb4c;
    --bark: #574a2c;
    --bark-text: #4a3e24;
    --cream: #ffffff;
    --teal: #7fc3cf;
    --rule: #b9b9b9;
    --lead: #e3ec9c;
    --fine: #d7e5a0;
  }
  * { box-sizing: border-box; margin: 0; padding: 0; }
  html, body { width: 1200px; height: 746px; overflow: hidden; }
  body {
    background: var(--stage);
    font-family: "PT Sans Narrow", "Arial Narrow", sans-serif;
    color: var(--bark-text);
    position: relative;
  }

  /* ---------- Front of postcard ---------- */
  .front {
    position: absolute; left: 37px; top: 37px;
    width: 432px; height: 664px;
    background: var(--sky);
    overflow: hidden;
    box-shadow: 0 2px 6px rgba(0,0,0,.18);
  }
  .front .hero {
    position: absolute; left: 0; top: 0; width: 432px; height: 245px;
    background: linear-gradient(160deg, #8a9aa6 0%, #5d6870 45%, #3a3f44 75%, #a3a9ae 100%);
  }
  .front .band-top {
    position: absolute; left: 0; top: 245px; width: 432px; height: 19px;
    background: var(--lime);
  }
  .logo-tab {
    position: absolute; background: var(--cream);
    display: flex; align-items: center; justify-content: center; gap: 8px;
    box-shadow: 0 2px 3px rgba(0,0,0,.15);
  }
  .front .logo-tab { left: 8px; top: 204px; width: 163px; height: 84px; border-radius: 6px 6px 22px 22px; }
  .logo-square { width: 18px; height: 18px; background: var(--teal); flex: none; }
  .logo-name { font-weight: 700; font-size: 17px; color: var(--bark); letter-spacing: .3px; }

  .services { position: absolute; left: 16px; top: 316px; }
  .services h2 { font-weight: 400; font-size: 19px; letter-spacing: .3px; margin-bottom: 6px; }
  .services li {
    list-style: none; font-size: 18px; line-height: 30px;
    display: flex; align-items: center; gap: 8px;
  }
  .services li::before {
    content: ""; width: 14px; height: 14px; border-radius: 50%; background: var(--lime);
  }

  .photo-circle { position: absolute; border-radius: 50%; border: 5px solid var(--cream); }
  .photo-bowl  { left: 281px; top: 250px; width: 132px; height: 132px;
    background: radial-gradient(circle at 40% 40%, #4d5a5e, #2a2f31 60%, #5f8a96); }
  .photo-park  { left: 187px; top: 321px; width: 134px; height: 134px;
    background: linear-gradient(180deg, #a9b6a0 0%, #7e9a62 55%, #5e8a3c 100%); }
  .photo-groom { left: 282px; top: 373px; width: 134px; height: 134px;
    background: radial-gradient(circle at 50% 55%, #b97a3e, #8a5a33 55%, #c9b8a6); }

  .offers {
    position: absolute; left: 0; top: 461px; width: 200px; height: 99px;
    background: var(--lime); border-radius: 0 8px 8px 0;
    border: 1px solid #e8f0c9; border-left: none;
    padding: 8px 10px 0 14px;
  }
  .offer { display: flex; align-items: baseline; gap: 4px; color: var(--bark-text); }
  .offer .pct { font-size: 14px; }
  .offer .what { font-size: 10px; }
  .offer-first { padding-bottom: 7px; border-bottom: 1px dotted var(--bark); }
  .offer-spa { justify-content: center; margin-top: 9px; }
  .disclaimer {
    position: absolute; left: 0; right: 0; bottom: 0; height: 19px;
    background: var(--fine); font-size: 5.5px; line-height: 6.5px; padding: 3px 6px 0 18px;
    border-radius: 0 0 8px 0;
  }

  .call-box { position: absolute; background: var(--bark); color: var(--cream); text-align: center; }
  .front .call-box {
    left: 221px; top: 528px; width: 211px; height: 59px;
    border-radius: 12px 0 0 12px; padding-top: 6px;
  }
  .call-lead { color: var(--lead); font-size: 12px; }
  .phone { display: flex; align-items: center; justify-content: center; gap: 7px; font-weight: 700; }
  .front .phone { font-size: 19px; margin-top: 3px; }
  .phone svg { flex: none; }

  .front .band-bottom {
    position: absolute; left: 0; top: 597px; width: 432px; height: 19px;
    background: var(--lime);
  }
  .front .footer {
    position: absolute; left: 16px; right: 16px; top: 626px;
    display: flex; justify-content: space-between; align-items: baseline;
  }
  .footer .address { font-size: 13px; }
  .footer .web { font-size: 16px; }

  /* ---------- Back of postcard ---------- */
  .back {
    position: absolute; left: 514px; top: 270px;
    width: 664px; height: 430px; background: var(--cream);
    box-shadow: 0 2px 6px rgba(0,0,0,.18);
  }
  .back .panel {
    position: absolute; left: 2px; top: 2px; width: 353px; height: 347px;
    background: var(--sky); border-radius: 0 0 10px 10px; overflow: hidden;
  }
  .back .logo-tab { left: 3px; top: 0; width: 160px; height: 84px; border-radius: 0 0 22px 22px; }
  .back .call { position: absolute; left: 178px; top: 28px; color: var(--bark-text); }
  .back .call .call-lead { color: var(--bark-text); font-size: 12px; }
  .back .phone { justify-content: flex-start; font-size: 19px; margin-top: 3px; }

  .grooming {
    position: absolute; left: 0; top: 104px; width: 353px; height: 136px;
    background: var(--lime); padding: 12px 10px 0 10px;
  }
  .grooming h3 { font-size: 10.5px; font-weight: 400; margin-bottom: 10px; letter-spacing: .2px; }
  .grooming-cols { display: flex; }
  .grooming ul { list-style: none; }
  .grooming ul:first-child { width: 195px; padding-left: 15px; }
  .grooming li { font-size: 11px; line-height: 18px; }
  .grooming li::before { content: "• "; }

  .location { position: absolute; left: 16px; top: 262px; width: 175px; }
  .location h3 { font-weight: 400; font-size: 16px; margin-bottom: 6px; }
  .location p { font-size: 10.5px; font-weight: 700; line-height: 16px; }
  .map {
    position: absolute; left: 199px; top: 252px; width: 142px; height: 80px;
    background: linear-gradient(135deg, #eceae4, #dcdad2);
  }
  .back .web-tab {
    position: absolute; left: 35px; top: 353px; width: 280px; height: 30px;
    background: var(--bark); color: var(--cream);
    border-radius: 0 0 12px 12px;
    display: flex; align-items: center; justify-content: center;
    font-size: 16px;
  }
  .stamp { position: absolute; left: 550px; top: 25px; width: 85px; height: 66px; border: 1px solid var(--rule); }
  .mail-line { position: absolute; left: 428px; width: 205px; height: 1px; background: var(--rule); }
  .mail-line.first { top: 204px; }
  .mail-line.second { top: 243px; }
  .mail-line.third { top: 281px; }
</style>
</head>
<body>

<section class="front" aria-label="Postcard front">
  <div class="hero" role="img" aria-label="Photo of a groomer trimming a small dark dog's paw with scissors"></div>
  <div class="band-top"></div>
  <div class="logo-tab"><span class="logo-square"></span><span class="logo-name">The Velvet Kennel</span></div>

  <div class="services">
    <h2>OUR SERVICES:</h2>
    <ul>
      <li>DOG GROOMING</li>
      <li>OVERNIGHT CARE</li>
      <li>DAYCARE</li>
    </ul>
  </div>

  <div class="photo-circle photo-bowl" role="img" aria-label="Photo of a dog drinking from a bowl"></div>
  <div class="photo-circle photo-park" role="img" aria-label="Photo of dogs playing on grass"></div>
  <div class="photo-circle photo-groom" role="img" aria-label="Photo of a golden dog being brushed"></div>

  <div class="offers">
    <div class="offer offer-first"><span class="pct">20%</span><span class="what">Off Your Pet's First Grooming Visit</span></div>
    <div class="offer offer-spa"><span class="pct">15%</span><span class="what">Off Any Spa Package</span></div>
    <p class="disclaimer">Limit one coupon per household. Not valid with any other offers or coupons. Other restriction or exclusions may apply, call for details.</p>
  </div>

  <div class="call-box">
    <p class="call-lead">Call Today For An Appointment</p>
    <p class="phone">
      <svg width="16" height="20" viewBox="0 0 16 20" aria-hidden="true"><path d="M14 2 H8 Q3 2 3 7 V13 M3 13 L0 9 M3 13 L6 9" fill="none" stroke="#fff" stroke-width="2.6" stroke-linecap="round" stroke-linejoin="round" transform="rotate(180 8 10)"/></svg>
      555-318-4096
    </p>
  </div>

  <div class="band-bottom"></div>
  <div class="footer">
    <span class="address">2847 Larkspur Lane Millbrook, WI 54900</span>
    <span class="web">www.PlumeRetreats.example</span>
  </div>
</section>

<section class="back" aria-label="Postcard back">
  <div class="panel">
    <div class="logo-tab"><span class="logo-square"></span><span class="logo-name">The Velvet Kennel</span></div>
    <div class="call">
      <p class="call-lead">Call Today For An Appointment</p>
      <p class="phone">
        <svg width="16" height="20" viewBox="0 0 16 20" aria-hidden="true"><path d="M14 2 H8 Q3 2 3 7 V13 M3 13 L0 9 M3 13 L6 9" fill="none" stroke="#574a2c" stroke-width="2.6" stroke-linecap="round" stroke-linejoin="round" transform="rotate(180 8 10)"/></svg>
        555-318-4096
      </p>
    </div>

    <div class="grooming">
      <h3>OUR GROOMING SERVICES:</h3>
      <div class="grooming-cols">
        <ul>
          <li>Organic Shampoo &amp; Conditioner</li>
          <li>Dental Care</li>
          <li>Soothing Mud Baths</li>
          <li>Flea &amp; Tick Preventative</li>
          <li>Shed-Less Treatment</li>
        </ul>
        <ul>
          <li>Nail Trim</li>
          <li>Haircut</li>
          <li>Paw Massage</li>
          <li>Spa Packages</li>
        </ul>
      </div>
    </div>

    <div class="location">
      <h3>The Velvet Kennel</h3>
      <p>Address: 2847 Larkspur Lane Millbrook, WI 54900. located in Millbrook.</p>
    </div>
    <div class="map" role="img" aria-label="Street map showing the kennel location in Millbrook"></div>
  </div>
  <div class="web-tab">www.PlumeRetreats.example</div>

  <div class="stamp"></div>
  <div class="mail-line first"></div>
  <div class="mail-line second"></div>
  <div class="mail-line third"></div>
</section>

</body>
</html>
```